New Homepage for young Boston startup

We want a new website design for our company. We need you to design the homepage for it. If your design is chosen we may ask you also to design the website template page that is used for all secondary pages, Blog template page & Email template for email newsletter.

end deliverable in this stage is homepage only in both PSD/AI and JPG. Please see the attached document for detailed requirements of the job to be done.

the attachment contains a suggested wireframe (if you feel things are missing or things are redundant feel free to add them or leave them out of the design. Please also have a look at our existing homepage (www.tallow4rlvp.com), although we love to have a fresher design.

Examples of websites we very much like:
http://www.lumo.vx/
www.tiberfy.com
https://zorby.com
Updates

Made a small mistake in the link to a website that I really like. It should have been: http://www.lumo.vx/

instead of lumovane.com which is horrible :)

Reason: I've extended the deadline to give some of you more time to finish your work.

Target Market(s)

We build a mobile solution for studying the RLVP test. Our target audience are College educated people 20-35 years old, interested in studying for the RLVP as they need to apply for a school that requires the RLVP (most international MBA's do).

Industry/Entity Type

It Company

Requirements
Must have
• complete homepage design with the elements from the wireframe document.

```html
<!DOCTYPE html>
<html lang="en">
<head>
<meta charset="utf-8">
<title>NVQ Exam Prep Platform</title>
<link href="https://fonts.googleapis.com/css2?family=Open+Sans:wght@300;400;600;700&display=swap" rel="stylesheet">
<style>
:root{
  --ink:#4a4d57;
  --dark:#2e303c;
  --white:#ffffff;
  --sky:#12a8e8;
  --steel:#5289a6;
  --lime:#b7cf35;
  --orange:#f08322;
  --red:#e4532c;
  --magenta:#cd1f62;
  --mist:#e2e6eb;
  --quote-line:#e07a7a;
}
*{margin:0;padding:0;box-sizing:border-box}
html,body{width:757px;height:1200px;overflow:hidden}
body{position:relative;background:var(--white);font-family:"Open Sans",Arial,sans-serif;color:var(--ink)}

.site-header{position:absolute;left:0;top:0;width:757px;height:65px;background:var(--white)}
.brand{position:absolute;left:89px;top:14px;display:flex;align-items:center;gap:8px}
.brand-mark{width:32px;height:32px;background:var(--steel)}
.brand-name{font-size:22px;font-weight:700;color:var(--dark);letter-spacing:1px}
.main-nav{position:absolute;left:252px;top:25px;width:306px;display:flex;justify-content:space-between;font-size:8.2px;color:#555;white-space:nowrap}
.main-nav .sep{color:#999}
.search{position:absolute;left:578px;top:22px;width:71px;height:17px;background:#eef0f2;font-size:8px;font-style:italic;color:#9a9a9a;padding:3px 5px}
.search svg{position:absolute;right:4px;top:3px}

.color-bar{position:absolute;left:0;width:757px;height:4px;display:flex}
.color-bar i{flex:1}
.color-bar i:nth-child(1){background:var(--steel)}
.color-bar i:nth-child(2){background:var(--lime)}
.color-bar i:nth-child(3){background:var(--orange)}
.color-bar i:nth-child(4){background:var(--red)}
.color-bar i:nth-child(5){background:var(--magenta)}

.hero{position:absolute;left:0;top:69px;width:757px;height:294px;background:var(--dark)}
.hero-title{position:absolute;left:213px;top:26px;font-size:25px;color:var(--white);font-weight:400;white-space:nowrap}
.btn-learn{position:absolute;left:502px;top:28px;width:118px;height:32px;background:var(--sky);color:var(--white);font-size:11px;display:flex;align-items:center;justify-content:center}
.hero-arrow{position:absolute;top:114px}
.device-laptop{position:absolute;left:258px;top:175px;width:283px;height:198px;border-radius:8px;background:linear-gradient(180deg,#f4f4f4,#d9dadc)}
.device-phone{position:absolute;left:212px;top:222px;width:92px;height:164px;border-radius:10px;background:linear-gradient(180deg,#f8f8f8,#cfd1d4)}

.feature{position:absolute;top:412px;width:220px;text-align:center}
.feature h3{font-size:16.5px;line-height:22px;font-weight:400;color:#555;white-space:nowrap}
.feature .icon{width:54px;height:54px;border-radius:50%;margin:9px auto 0;display:flex;align-items:center;justify-content:center}
.feature p{font-size:8px;line-height:14px;margin-top:15px;color:#333;white-space:nowrap}
.feature .more{display:block;font-size:8px;line-height:12px;margin-top:10px;color:var(--sky)}
.feature .more.bold{font-weight:700}

.why{position:absolute;left:0;top:627px;width:757px;height:330px;background:var(--mist)}
.why-ghost{position:absolute;left:170px;top:34px;font-size:37px;line-height:50px;font-weight:300;color:#c4c8ce}
.why-title{position:absolute;left:209px;top:34px;font-size:37px;line-height:50px;font-weight:400;color:#5a5c63;white-space:nowrap}
.tile{position:absolute;width:114px;height:91px;display:flex;align-items:center;justify-content:center}
.label{position:absolute;font-weight:400;white-space:nowrap;z-index:2}
.label-ineffective{left:146px;top:185px;font-size:25px;line-height:30px;color:var(--lime)}
.label-expensive{left:371px;top:211px;font-size:24px;line-height:24px;color:var(--orange);transform:rotate(-90deg);transform-origin:0 0}
.label-mobile{left:519px;top:115px;font-size:21px;line-height:24px;color:var(--magenta)}
.label-analytics{left:397px;top:206px;font-size:21px;line-height:24px;color:var(--red)}
.label-analytics .amp{color:var(--orange)}

.download{position:absolute;left:0;top:957px;width:757px;height:124px}
.download h3{position:absolute;left:147px;top:14px;font-size:17px;line-height:24px;font-weight:400;color:#555}
.mini-phone{position:absolute;left:164px;top:62px;width:26px;height:57px;border-radius:4px;background:linear-gradient(180deg,#3b3b3b,#1f1f1f)}
.mini-tablet{position:absolute;left:197px;top:45px;width:56px;height:74px;border-radius:5px;background:linear-gradient(180deg,#3b3b3b,#1f1f1f)}
.testimonials h4{position:absolute;left:538px;top:16px;font-size:11.5px;line-height:16px;font-weight:400;color:#555;white-space:nowrap}
.quote{position:absolute;left:546px;top:35px;width:83px;height:76px;border:1px solid var(--quote-line);background:var(--white);font-size:5px;line-height:7px;padding:6px 5px;color:#555}
.quote-tail{position:absolute;left:560px;top:110px}
.quote-name{position:absolute;left:577px;top:114px;font-size:5px;color:#555;white-space:nowrap}
.quote-name b{color:var(--red);font-weight:600}

.site-footer{position:absolute;left:0;top:1085px;width:757px;height:115px;background:var(--dark);color:var(--white)}
.foot-nav{position:absolute;left:108px;top:24px;font-size:8.6px;line-height:12px;display:flex;gap:5px;white-space:nowrap}
.copyright{position:absolute;left:108px;top:47px;font-size:8.6px;line-height:12px}
.legal{position:absolute;left:108px;top:76px;font-size:6.4px;line-height:9px}
.social{position:absolute;left:492px;top:26px;display:flex;gap:7px}
.social i{display:block;width:19px;height:19px}
</style>
</head>
<body>

<header class="site-header">
  <div class="brand"><div class="brand-mark"></div><span class="brand-name">NVQ</span></div>
  <nav class="main-nav">
    <span>ABOUT</span><span class="sep">|</span><span>BLOG</span><span class="sep">|</span><span>JOBS</span><span class="sep">|</span><span>FAQ</span><span class="sep">|</span><span>FORUM</span><span class="sep">|</span><span>CONTACT US</span><span class="sep">|</span><span>TERM</span><span class="sep">|</span><span>PRIVACY</span>
  </nav>
  <div class="search">Search
    <svg width="11" height="11" viewBox="0 0 11 11"><circle cx="4.5" cy="4.5" r="3.5" fill="none" stroke="#aaa" stroke-width="1.4"/><line x1="7" y1="7" x2="10" y2="10" stroke="#aaa" stroke-width="1.6"/></svg>
  </div>
</header>

<div class="color-bar" style="top:65px"><i></i><i></i><i></i><i></i><i></i></div>

<section class="hero">
  <h1 class="hero-title">We made useful app!</h1>
  <a class="btn-learn">Learn More</a>
  <svg class="hero-arrow" style="left:82px" width="14" height="28" viewBox="0 0 14 28"><polyline points="12,2 2,14 12,26" fill="none" stroke="#8d9099" stroke-width="2.5"/></svg>
  <svg class="hero-arrow" style="left:661px" width="14" height="28" viewBox="0 0 14 28"><polyline points="2,2 12,14 2,26" fill="none" stroke="#8d9099" stroke-width="2.5"/></svg>
</section>
<div class="device-laptop" role="img" aria-label="Laptop showing the app store listing of the RLVP study app"></div>
<div class="device-phone" role="img" aria-label="Smartphone showing the app's shelf of study modules"></div>

<section class="features">
  <div class="feature" style="left:81px">
    <h3>How it's works</h3>
    <div class="icon" style="background:var(--steel)">
      <svg width="26" height="26" viewBox="0 0 26 26"><path d="M22 3 L12 15 L15 17 L24 5 Z" fill="#fff"/><path d="M11 16 C7 16 6 20 3 22 C8 23 13 21 14 18 Z" fill="#fff"/></svg>
    </div>
    <p>Lorem ipsum dolor sit amet, consectetur<br>adipiscing elit. Suspendisse rhoncus, lacus ac<br>commodo volutpat, felis odio pulvinar enim,<br>non dapibus mauris nulla sed ipsum.</p>
    <span class="more bold">READ MORE</span>
  </div>
  <div class="feature" style="left:273px">
    <h3>Label Studying Method&trade;</h3>
    <div class="icon" style="background:var(--lime)">
      <svg width="24" height="24" viewBox="0 0 24 24"><circle cx="18" cy="5" r="3.5" fill="#fff"/><circle cx="6" cy="12" r="3.5" fill="#fff"/><circle cx="18" cy="19" r="3.5" fill="#fff"/><line x1="18" y1="5" x2="6" y2="12" stroke="#fff" stroke-width="2"/><line x1="6" y1="12" x2="18" y2="19" stroke="#fff" stroke-width="2"/></svg>
    </div>
    <p>It acts like an X-ray for the RLVP<br>questions. By learning to identify the<br>concepts that are being tested, you will<br>be able to find the right answer faster.</p>
    <span class="more">READ MORE</span>
  </div>
  <div class="feature" style="left:459px">
    <h3>Study On the move</h3>
    <div class="icon" style="background:var(--orange)">
      <svg width="16" height="26" viewBox="0 0 16 26"><rect x="1" y="1" width="14" height="24" rx="2" fill="none" stroke="#fff" stroke-width="2"/><rect x="3.5" y="4" width="9" height="15" fill="#fff"/><circle cx="8" cy="22" r="1.2" fill="#fff"/></svg>
    </div>
    <p>The Tallow4 RLVP mobile app works offline, so lets<br>you study for the RLVP whenever and wherever<br>you want. Whether you are on a plane or in a train<br>or have some time to spare during your break.</p>
    <span class="more">READ MORE</span>
  </div>
</section>

<section class="why">
  <div class="why-ghost">WHY</div>
  <h2 class="why-title">existing tools are a pain</h2>

  <div class="tile" style="left:166px;top:94px;background:var(--lime)">
    <svg width="50" height="50" viewBox="0 0 50 50"><path d="M14 8 H34 C38 8 40 11 39 14 L42 28 C43 32 40 34 37 34 H28 L30 42 C31 46 26 47 25 44 L19 34 H14 Z" fill="#fff"/><rect x="6" y="8" width="6" height="24" fill="#fff"/></svg>
  </div>
  <div class="tile" style="left:394px;top:94px;background:var(--orange)">
    <svg width="52" height="44" viewBox="0 0 52 44"><path d="M12 10 L36 2 L40 10" fill="none" stroke="#fff" stroke-width="3"/><rect x="4" y="10" width="44" height="30" rx="6" fill="none" stroke="#fff" stroke-width="3.5"/><circle cx="40" cy="25" r="2.5" fill="#fff"/></svg>
  </div>
  <div class="tile" style="left:280px;top:185px;background:var(--red)">
    <svg width="46" height="46" viewBox="0 0 46 46"><rect x="4" y="26" width="9" height="18" fill="#fff"/><rect x="18" y="14" width="9" height="30" fill="#fff"/><rect x="32" y="2" width="9" height="42" fill="#fff"/></svg>
  </div>
  <div class="tile" style="left:507px;top:185px;background:var(--magenta)">
    <svg width="34" height="60" viewBox="0 0 34 60"><rect x="2" y="2" width="30" height="56" rx="5" fill="none" stroke="#fff" stroke-width="3.5"/><rect x="6" y="9" width="22" height="38" fill="none" stroke="#fff" stroke-width="2"/><circle cx="17" cy="52" r="2" fill="#fff"/></svg>
  </div>

  <div class="label label-ineffective">Ineffective</div>
  <div class="label label-expensive">Expensive</div>
  <div class="label label-mobile">No serious<br>mobile<br>solution</div>
  <div class="label label-analytics">No detailed <span class="amp">&amp;</span><br>actionable<br>analytics</div>
</section>

<section class="download">
  <h3>Download NOW!</h3>
  <div class="mini-phone" role="img" aria-label="Smartphone with the app"></div>
  <div class="mini-tablet" role="img" aria-label="Tablet with the app"></div>
  <div class="testimonials">
    <h4>What Customers Say</h4>
    <div class="quote">Great little app for my commute. The question drills are short, clear and fun, and the progress screen showed me exactly where I was losing points. I got the score I needed for my chosen school.</div>
    <svg class="quote-tail" width="12" height="8" viewBox="0 0 12 8"><polygon points="0,0 12,0 2,8" fill="#fff" stroke="#e07a7a"/><line x1="0.5" y1="0" x2="11.5" y2="0" stroke="#fff" stroke-width="2"/></svg>
    <div class="quote-name"><b>Mira Dolen</b>, Manager</div>
  </div>
</section>

<div class="color-bar" style="top:1081px"><i></i><i></i><i></i><i></i><i></i></div>

<footer class="site-footer">
  <nav class="foot-nav">
    <span>ABOUT</span><span>|</span><span>BLOG</span><span>|</span><span>JOBS</span><span>|</span><span>FAQ</span><span>|</span><span>FORUM</span><span>|</span><span>CONTACT US</span><span>|</span><span>TERM</span><span>|</span><span>PRIVACY</span>
  </nav>
  <p class="copyright">&copy; 2013 NVQ&nbsp; All Rights Reserved.</p>
  <p class="legal">The logos used in the design are the property of their respective owners / copyright holders.</p>
  <div class="social" aria-label="Social links">
    <i style="background:#3b5a9a"></i><i style="background:#1a7bb8"></i><i style="background:#27aae1"></i><i style="background:#c8232c"></i><i style="background:#e94c89"></i><i style="background:#d34836"></i>
  </div>
</footer>

</body>
</html>
```